International gaming entertainment company is looking for an innovative Power Point design *

We are looking for a Power Point design for potential international investors, partners and customers in the gaming industry, meaning that a reference to internationality and gaming should become apparent.
The template should be in a reduced and clear style with a combination of innovation and tradition. It should be adaptive and suitable for various applications (tables, shapes and diagrams).
The color scheme of our company are various shades of gray and burgundy (wine-red), however as for the design in question, we are open to other meaningful suggestions (no garish colors).
Updates

Noch kein Design dabei, dass uns 100%ig überzeugt

Target Market(s)

International investors and partners in the gaming industry

Font styles to use
Serif
Sans Serif
Other font styles liked:
• Interstate

Requirements
Must have
• Clear lines
Modern
Footer line with room for classification (eg Confidential, Public) and page number

```html
<!DOCTYPE html>
<html lang="en">
<head>
<meta charset="utf-8">
<title>Velora Gaming International – Presentation Template</title>
<link href="https://fonts.googleapis.com/css2?family=Oswald:wght@300;400;500;600&family=Roboto:wght@300;400;500;700&display=swap" rel="stylesheet">
<style>
:root{
  --red:#e30613;
  --red-dark:#b1000c;
  --ink:#2b2b2b;
  --text:#6f6f6f;
  --grey:#bdbdbd;
  --grey-dark:#4a4a4a;
  --paper:#f5f5f7;
  --canvas:#e7e7ea;
  --line:#e2e2e5;
  --stone:#d2d2d6;
}
*{box-sizing:border-box;margin:0;padding:0}
html,body{width:1200px;height:4841px;overflow:hidden;background:var(--canvas)}
body{font-family:"Roboto",sans-serif;color:var(--ink)}
.deck{display:grid;grid-template-columns:564px 564px;grid-auto-rows:319px;column-gap:22px;row-gap:25px;padding:28px 24px 0}
.slide{position:relative;overflow:hidden;background:var(--paper)}
.abs{position:absolute}
.title{position:absolute;left:26px;top:12px;right:0;font-family:"Oswald",sans-serif;font-weight:400;font-size:17px;letter-spacing:.3px;color:var(--ink);padding-bottom:6px;border-bottom:1px solid var(--line)}
.title.red{color:var(--red)}
.lorem{font-size:6px;line-height:1.6;color:var(--text)}
.foot{position:absolute;left:24px;right:22px;bottom:9px;height:16px;display:flex;align-items:center;gap:12px;font-size:5px;color:#777}
.foot-mark{display:flex;align-items:center;gap:4px;font-family:"Oswald",sans-serif;font-size:8px;color:var(--red);letter-spacing:.5px}
.foot-mark i{display:block;width:10px;height:10px;border-radius:50%;background:var(--red)}
.foot-page{margin-left:auto;color:var(--red);font-size:6px;border-bottom:1px solid var(--red);width:26px;text-align:right;padding-bottom:2px}
.square{position:absolute;background:var(--red);display:flex;align-items:center;justify-content:center}
.photo{position:absolute}
.brand-disc{position:absolute;border-radius:50%;background:var(--red);display:flex;align-items:center;justify-content:center;font-family:"Oswald",sans-serif;color:#fff;letter-spacing:2px}
.heading-xl{font-family:"Oswald",sans-serif;font-weight:400;line-height:1.15}
.tag{position:absolute;top:28px;right:28px;background:var(--red);color:#fff;font-family:"Oswald",sans-serif;font-size:9px;padding:3px 14px}
.giant{position:absolute;left:24px;right:24px;top:52px;font-family:"Oswald",sans-serif;font-weight:600;font-size:84px;letter-spacing:4px;color:#d6d6da;text-align:center;line-height:1}
.section-label{position:absolute;right:40px;bottom:52px;font-family:"Oswald",sans-serif;color:var(--red);font-size:13px;border-top:1px solid var(--red);padding-top:6px;width:110px;text-align:right}
.small-red{color:var(--red);font-family:"Oswald",sans-serif}
table.data{position:absolute;left:60px;top:78px;border-collapse:collapse;font-size:6px;color:#666}
table.data th{background:var(--red);color:#fff;font-weight:400;padding:4px 10px;text-align:center}
table.data th.blank{background:none}
table.data td{padding:3px 10px;text-align:center;border-bottom:1px solid var(--line)}
table.data td.label{background:var(--red);color:#fff;text-align:left;border-bottom:1px solid #fff}
table.data td.soft{background:#eee}
.bar-row{position:absolute;left:0;right:0;height:12px}
.bar-row span{position:absolute;left:0;top:0;font-size:6px;color:#555}
.bar-row b{position:absolute;right:0;top:0;font-size:6px;color:#555;font-weight:400}
.bar-row .track{position:absolute;left:0;right:0;top:9px;height:3px;background:#e0e0e0}
.bar-row .fill{position:absolute;left:0;top:9px;height:3px;background:var(--red)}
.num-item{position:absolute;width:220px;height:40px}
.num-item .n{position:absolute;left:0;top:0;width:22px;height:22px;background:var(--red);color:#fff;font-size:9px;display:flex;align-items:center;justify-content:center}
.num-item h4{position:absolute;left:36px;top:0;font-size:5.5px;color:var(--red);letter-spacing:1px;font-weight:500}
.num-item p{position:absolute;left:36px;top:9px;width:180px}
</style>
</head>
<body>
<main class="deck">

<!-- 1 Cover -->
<section class="slide" style="background:#fff">
  <div class="abs" style="left:0;right:0;top:0;height:26px;background:var(--red)"></div>
  <div class="abs" style="left:0;right:0;bottom:0;height:58px;background:var(--red)"></div>
  <div class="abs" style="left:300px;top:-10px;width:320px;height:300px;border-radius:50%;background:#ececef"></div>
  <div class="brand-disc" style="left:368px;top:52px;width:172px;height:172px;font-size:22px">VELORA</div>
  <div class="abs heading-xl" style="left:22px;top:108px;font-size:25px;color:var(--ink)">INTERNATIONAL<br>GAMING ENTERTAINMENT</div>
  <div class="abs" style="left:24px;top:175px;font-size:6px;letter-spacing:2.5px;color:#555">Presentation Template</div>
  <div class="abs" style="left:24px;bottom:12px;display:flex;gap:4px;align-items:center">
    <i style="width:10px;height:10px;border-radius:50%;background:#fff;display:block"></i>
    <i style="width:10px;height:10px;border-radius:50%;background:#fff;display:block"></i>
    <i style="width:10px;height:10px;border-radius:50%;background:#fff;display:block"></i>
    <span style="font-size:5px;color:#fff;margin-left:18px">Add your classification details here (Confidential or Public)</span>
  </div>
</section>

<!-- 2 Cover alt -->
<section class="slide" style="background:var(--stone)">
  <div class="abs heading-xl" style="left:0;right:0;top:42px;text-align:center;font-size:38px;color:#5a5a5e">INTERNATIONAL GAMING<br>ENTERTAINMENT</div>
  <div class="abs" style="left:0;right:0;top:150px;text-align:center;font-size:6px;letter-spacing:2.5px;color:#444">Presentation Template</div>
  <div class="abs" style="left:0;right:0;top:192px;text-align:center;font-family:'Oswald',sans-serif;font-size:16px;color:var(--red)">VELORA GAMING INTERNATIONAL</div>
</section>

<!-- 3 Master -->
<section class="slide" style="background:#fff">
  <div class="abs" style="left:0;right:0;top:40px;bottom:46px;background:var(--red)"></div>
  <div class="abs" style="left:330px;top:40px;width:240px;height:233px;border-radius:50%;background:rgba(255,255,255,.12)"></div>
  <div class="brand-disc" style="left:340px;top:70px;width:172px;height:172px;background:#fff;color:var(--red);font-size:22px">VELORA</div>
  <div class="abs heading-xl" style="left:22px;top:112px;font-size:26px;color:#fff">MASTER SLIDE<br>PRESENTATION</div>
  <div class="abs" style="left:22px;top:190px;font-size:6px;letter-spacing:2px;color:#fff">2020</div>
  <div class="abs" style="left:22px;top:205px;width:26px;height:1px;background:#fff"></div>
</section>

<!-- 4 Agenda -->
<section class="slide" style="background:#fff">
  <h2 class="title red">AGENDA</h2>
  <ul class="abs" style="left:80px;top:76px;list-style:none;font-size:6px;color:#444;line-height:20px">
    <li><span class="small-red">● </span>Introduction</li>
    <li><span class="small-red">● </span>About Us</li>
    <li><span class="small-red">● </span>Welcome Message</li>
    <li><span class="small-red">● </span>Company</li>
    <li><span class="small-red">● </span>Management</li>
    <li><span class="small-red">● </span>Operations</li>
    <li><span class="small-red">● </span>Careers</li>
    <li><span class="small-red">● </span>Info graphic Charts</li>
    <li><span class="small-red">● </span>Contact Us</li>
  </ul>
  <div class="photo" role="img" aria-label="Oval photo of casino dice and gaming chips" style="left:282px;top:70px;width:262px;height:148px;border-radius:50%;background:linear-gradient(135deg,#3a3a3a,#8a1a20 55%,#2a2a2a)"></div>
  <footer class="foot"><span class="foot-mark"><i></i>VELORA</span><span>Add your classification details here (Confidential or Public)</span><span class="foot-page">4</span></footer>
</section>

<!-- 5 About -->
<section class="slide">
  <h2 class="title">ABOUT US</h2>
  <div class="abs" style="left:0;top:46px;width:158px;height:220px;background:var(--red);color:#fff;font-family:'Oswald',sans-serif">
    <div style="position:absolute;left:30px;top:34px;font-size:26px;font-weight:300">3,800</div>
    <div style="position:absolute;left:48px;top:70px;font-size:5px;letter-spacing:.5px">GAMING MACHINES</div>
    <div style="position:absolute;left:30px;top:90px;font-size:26px;font-weight:300">23</div>
    <div style="position:absolute;left:48px;top:126px;font-size:5px;letter-spacing:.5px">LICENSED CASINOS</div>
    <div style="position:absolute;left:30px;top:146px;font-size:26px;font-weight:300">270</div>
    <div style="position:absolute;left:48px;top:182px;font-size:5px;letter-spacing:.5px">GAMING TABLES</div>
  </div>
  <p class="abs lorem" style="left:212px;top:78px;width:310px">Lorem ipsum dolor sit amet, consectetuer adipiscing elit, sed diam nonummy nibh euismod tincidunt ut laoreet dolore magna aliquam erat volutpat. Ut wisi enim ad minim veniam, quis nostrud exerci tation ullamcorper suscipit lobortis nisl ut aliquip ex ea commodo consequat. Duis autem vel eum iriure dolor in hendrerit in vulputate velit esse molestie consequat.</p>
  <p class="abs lorem" style="left:212px;top:160px;width:310px">Lorem ipsum dolor sit amet, consectetuer adipiscing elit, sed diam nonummy nibh euismod tincidunt ut laoreet dolore magna aliquam erat volutpat. Ut wisi enim ad minim veniam, quis nostrud exerci tation ullamcorper suscipit lobortis nisl ut aliquip ex ea commodo consequat. Duis autem vel eum iriure dolor in hendrerit in vulputate velit esse molestie consequat.</p>
  <footer class="foot"><span class="foot-mark"><i></i>VELORA</span><span>Add your classification details here (Confidential or Public)</span><span class="foot-page">5</span></footer>
</section>

<!-- 6 What we do -->
<section class="slide" style="background:#fff">
  <h2 class="title">WHAT WE DO</h2>
  <svg class="abs" style="left:26px;top:90px" width="22" height="22" viewBox="0 0 22 22"><circle cx="11" cy="11" r="9" fill="none" stroke="#555" stroke-width="1.5"/><circle cx="11" cy="11" r="4" fill="none" stroke="#555" stroke-width="1.5"/></svg>
  <p class="abs lorem" style="left:26px;top:124px;width:180px">Lorem ipsum dolor sit amet, consectetuer adipiscing elit, sed diam nonummy nibh euismod tincidunt ut laoreet dolore magna aliquam erat volutpat. Ut wisi enim ad minim veniam, quis nostrud exerci tation ullamcorper suscipit lobortis nisl ut aliquip ex ea commodo consequat. Duis autem vel eum iriure dolor in hendrerit in vulputate velit esse molestie consequat.</p>
  <div class="photo" role="img" aria-label="Black and white photo of playing cards and casino chips" style="left:224px;top:50px;width:92px;height:170px;background:linear-gradient(160deg,#8a8a8a,#2a2a2a)"></div>
  <div class="abs small-red" style="left:352px;top:80px;font-size:8px">OUR CORE VALUES:</div>
  <div class="square" style="left:358px;top:106px;width:34px;height:34px"><svg width="16" height="16" viewBox="0 0 16 16"><path d="M8 1 14 8 8 15 2 8Z" fill="#fff"/></svg></div>
  <div class="abs lorem" style="left:356px;top:144px">Lorem ipsum</div>
  <div class="square" style="left:460px;top:106px;width:34px;height:34px"><svg width="16" height="16" viewBox="0 0 16 16"><path d="M8 1C5 5 2 7 2 10a3 3 0 0 0 5 2l-1 3h4l-1-3a3 3 0 0 0 5-2c0-3-3-5-6-9Z" fill="#fff"/></svg></div>
  <div class="abs lorem" style="left:458px;top:144px">Lorem ipsum</div>
  <div class="square" style="left:358px;top:182px;width:34px;height:34px"><svg width="16" height="16" viewBox="0 0 16 16"><circle cx="8" cy="4.5" r="3" fill="#fff"/><circle cx="4.5" cy="9" r="3" fill="#fff"/><circle cx="11.5" cy="9" r="3" fill="#fff"/><path d="M7 9h2l1 6H6Z" fill="#fff"/></svg></div>
  <div class="abs lorem" style="left:356px;top:220px">Lorem ipsum</div>
  <div class="square" style="left:460px;top:182px;width:34px;height:34px"><svg width="16" height="16" viewBox="0 0 16 16"><path d="M8 15 2 8a3.3 3.3 0 0 1 6-4 3.3 3.3 0 0 1 6 4Z" fill="#fff"/></svg></div>
  <div class="abs lorem" style="left:458px;top:220px">Lorem ipsum</div>
  <footer class="foot"><span class="foot-mark"><i></i>VELORA</span><span>Add your classification details here (Confidential or Public)</span><span class="foot-page">6</span></footer>
</section>

<!-- 7 Four decades -->
<section class="slide" style="background:#fff">
  <h2 class="title red">FOUR DECADES OF SUCCESS</h2>
  <div class="photo" role="img" aria-label="Illustration of a magnifying glass over a red playing card emblem" style="left:4px;top:68px;width:250px;height:196px;background:linear-gradient(135deg,#d9d3cc,#f1eeea 50%,#e9c3c5)"></div>
  <p class="abs lorem" style="left:280px;top:106px;width:252px">Lorem ipsum dolor sit amet, consectetuer adipiscing elit, sed diam nonummy nibh euismod tincidunt ut laoreet dolore magna aliquam erat volutpat. Ut wisi enim ad minim veniam, quis nostrud exerci tation ullamcorper suscipit lobortis nisl ut aliquip ex ea commodo consequat. Duis autem vel eum iriure dolor in hendrerit in vulputate velit esse molestie consequat.</p>
  <div class="abs" style="left:280px;top:216px;width:110px;height:18px;border-radius:9px;background:var(--red);color:#fff;font-size:6px;letter-spacing:1.5px;display:flex;align-items:center;justify-content:center">LEARN MORE</div>
  <footer class="foot"><span class="foot-mark"><i></i>VELORA</span><span>Add your classification details here (Confidential or Public)</span><span class="foot-page">7</span></footer>
</section>

<!-- 8 Section Company -->
<section class="slide" style="background:#fff">
  <div class="tag">SECTION 01</div>
  <div class="giant">COMPANY</div>
  <div class="square" style="left:46px;top:182px;width:34px;height:34px"><svg width="18" height="18" viewBox="0 0 18 18" fill="none" stroke="#fff" stroke-width="1.4"><rect x="2" y="3" width="14" height="12"/><path d="M5 6h2M11 6h2M5 9h2M11 9h2M5 12h2M11 12h2"/></svg></div>
  <p class="abs lorem" style="left:110px;top:180px;width:420px">Lorem ipsum dolor sit amet, consectetuer adipiscing elit, sed diam nonummy nibh euismod tincidunt ut laoreet dolore magna aliquam erat volutpat. Ut wisi enim ad minim veniam, quis nostrud exerci tation ullamcorper suscipit lobortis nisl ut aliquip ex ea commodo consequat. Duis autem vel eum iriure dolor in hendrerit in vulputate velit esse molestie consequat.</p>
  <div class="section-label" style="bottom:32px">COMPANY</div>
</section>

<!-- 9 Bar chart -->
<section class="slide" style="background:#fff">
  <h2 class="title">BAR CHART</h2>
  <svg class="abs" style="left:22px;top:62px" width="330" height="180" viewBox="0 0 330 180" font-size="5" fill="#888" font-family="Roboto,sans-serif">
    <g stroke="#eee"><line x1="20" y1="10" x2="320" y2="10"/><line x1="20" y1="40" x2="320" y2="40"/><line x1="20" y1="70" x2="320" y2="70"/><line x1="20" y1="100" x2="320" y2="100"/><line x1="20" y1="130" x2="320" y2="130"/></g>
    <line x1="20" y1="160" x2="320" y2="160" stroke="#bbb"/>
    <text x="4" y="12">120</text><text x="4" y="42">100</text><text x="8" y="72">80</text><text x="8" y="102">60</text><text x="8" y="132">40</text><text x="8" y="162">20</text>
    <g fill="#e30613"><rect x="30" y="40" width="8" height="120"/><rect x="66" y="70" width="8" height="90"/><rect x="102" y="25" width="8" height="135"/><rect x="138" y="10" width="8" height="150"/><rect x="174" y="70" width="8" height="90"/><rect x="210" y="30" width="8" height="130"/><rect x="246" y="82" width="8" height="78"/><rect x="282" y="100" width="8" height="60"/></g>
    <g fill="#bdbdbd"><rect x="40" y="20" width="8" height="140"/><rect x="76" y="40" width="8" height="120"/><rect x="112" y="100" width="8" height="60"/><rect x="148" y="10" width="8" height="150"/><rect x="184" y="20" width="8" height="140"/><rect x="220" y="10" width="8" height="150"/><rect x="256" y="30" width="8" height="130"/><rect x="292" y="10" width="8" height="150"/></g>
    <text x="30" y="172">Jan</text><text x="66" y="172">Mar</text><text x="102" y="172">Apr</text><text x="138" y="172">Mai</text><text x="174" y="172">Jun</text><text x="210" y="172">Jul</text><text x="246" y="172">Aug</text><text x="282" y="172">Sep</text>
  </svg>
  <div class="abs" style="left:364px;top:46px;right:0;height:164px;background:#e3e3e6"></div>
  <div class="square" style="left:508px;top:36px;width:26px;height:26px;background:#fff;border:1px solid var(--line)"><svg width="16" height="16" viewBox="0 0 16 16" fill="none" stroke="#e30613" stroke-width="1.4"><circle cx="8" cy="8" r="6"/><circle cx="8" cy="8" r="3"/><path d="M8 8 14 2"/></svg></div>
  <div class="abs" style="left:388px;top:100px;font-family:'Oswald',sans-serif;font-size:14px;color:#444">LOREM IPSUM</div>
  <p class="abs lorem" style="left:388px;top:122px;width:150px">Lorem ipsum dolor sit amet, consectetuer adipiscing elit, sed diam nonummy nibh euismod tincidunt ut laoreet dolore magna aliquam erat volutpat. Ut wisi enim ad minim veniam, quis nostrud exerci tation suscipit lobortis nisl ut aliquip ex ea commodo consequat.</p>
  <footer class="foot"><span class="foot-mark"><i></i>VELORA</span><span>Add your classification details here (Confidential or Public)</span><span class="foot-page">9</span></footer>
</section>

<!-- 10 Pie chart -->
<section class="slide" style="background:#fff">
  <h2 class="title">PIE CHART</h2>
  <div class="abs" style="left:140px;top:62px;font-size:7px;color:#666">Your Text here</div>
  <svg class="abs" style="left:40px;top:78px" width="240" height="170" viewBox="0 0 240 170" font-family="Roboto,sans-serif">
    <g transform="translate(75,75) rotate(-70)">
      <circle r="35" fill="none" stroke="#e30613" stroke-width="70" pathLength="100" stroke-dasharray="60 40" stroke-dashoffset="-40"/>
      <circle r="35" fill="none" stroke="#e4e3ef" stroke-width="70" pathLength="100" stroke-dasharray="22 78" stroke-dashoffset="0"/>
      <circle r="35" fill="none" stroke="#2b2b2b" stroke-width="70" pathLength="100" stroke-dasharray="18 82" stroke-dashoffset="-22"/>
    </g>
    <text x="75" y="36" font-size="9" fill="#444">22%</text>
    <text x="100" y="80" font-size="9" fill="#fff">18%</text>
    <text x="28" y="104" font-size="9" fill="#fff">60%</text>
    <rect x="170" y="38" width="42" height="48" fill="#9e9e9e"/><rect x="170" y="86" width="42" height="40" fill="#d0d0d0"/>
    <text x="182" y="66" font-size="9" fill="#fff">10%</text><text x="184" y="110" font-size="9" fill="#555">8%</text>
    <line x1="140" y1="42" x2="170" y2="38" stroke="#aaa" stroke-width=".6"/><line x1="140" y1="110" x2="170" y2="126" stroke="#aaa" stroke-width=".6"/>
    <text x="30" y="160" font-size="5" fill="#888">● 1st Qtr   ● 2nd Qtr   ● 3rd Qtr   ● 4th Qtr</text>
  </svg>
  <div class="abs" style="left:330px;top:80px;width:200px">
    <div class="small-red" style="font-size:7px">Insert title here</div>
    <p class="lorem" style="margin-bottom:12px">There are many variations of passages of lorem ipsum available, but the majority have suffered alteration in some form, est.</p>
    <div style="font-size:7px;color:#444">Insert title here</div>
    <p class="lorem" style="margin-bottom:12px">There are many variations of passages of lorem ipsum available, but the majority have suffered alteration in some form, est.</p>
    <div style="font-size:7px;color:#999">Insert title here</div>
    <p class="lorem">There are many variations of passages of lorem ipsum available, but the majority have suffered alteration in some form, est.</p>
  </div>
  <footer class="foot"><span class="foot-mark"><i></i>VELORA</span><span>Add your classification details here (Confidential or Public)</span><span class="foot-page">10</span></footer>
</section>

<!-- 11 Photo with panel -->
<section class="slide">
  <div class="photo" role="img" aria-label="Photo of a blue glass casino building with a neon sign" style="inset:0;background:linear-gradient(135deg,#0b3c8c,#2c72c9 55%,#0a2f6b)"></div>
  <div class="abs" style="left:286px;top:36px;width:256px;height:234px;background:rgba(255,255,255,.78);border:6px solid #fff"></div>
  <div class="abs" style="left:312px;top:64px;width:210px">
    <div style="font-family:'Oswald',sans-serif;font-size:10px;color:#333">GOALS</div>
    <div style="font-size:5.5px;color:#333;margin:6px 0 2px 24px;letter-spacing:1px">LOREM IPSUM DOLOR</div>
    <p class="lorem" style="margin-left:24px;color:#444">Lorem ipsum dolor sit amet, consectetuer adipiscing elit, sed diam nonummy nibh euismod tincidunt ut laoreet dolore magna aliquam erat volutpat.</p>
    <div style="font-family:'Oswald',sans-serif;font-size:10px;color:#333;margin-top:30px">GAMING</div>
    <div style="font-size:5.5px;color:#333;margin:6px 0 2px 24px;letter-spacing:1px">LOREM IPSUM DOLOR</div>
    <p class="lorem" style="margin-left:24px;color:#444">Lorem ipsum dolor sit amet, consectetuer adipiscing elit, sed diam nonummy nibh euismod tincidunt ut laoreet dolore magna aliquam erat volutpat.</p>
  </div>
</section>

<!-- 12 Goals / laptop -->
<section class="slide" style="background:#fff">
  <div class="abs" style="left:38px;top:60px;width:250px">
    <div style="font-family:'Oswald',sans-serif;font-size:10px;color:#333">Goals</div>
    <div style="display:flex;gap:10px;margin-top:8px"><svg width="14" height="14" viewBox="0 0 14 14" fill="none" stroke="#555"><path d="M3 2h8v4a4 4 0 0 1-8 0Z"/><path d="M7 10v2M4 13h6"/></svg>
      <div><div style="font-size:5.5px;color:#333;letter-spacing:.5px;margin-bottom:2px">LOREM IPSUM DOLOR</div><p class="lorem">Lorem ipsum dolor sit amet, consectetuer adipiscing elit, sed diam nonummy nibh euismod tincidunt ut laoreet dolore magna aliquam erat volutpat.</p></div></div>
    <div style="font-family:'Oswald',sans-serif;font-size:10px;color:#333;margin-top:22px">Gaming</div>
    <div style="display:flex;gap:10px;margin-top:8px"><svg width="14" height="14" viewBox="0 0 14 14" fill="none" stroke="#555"><rect x="2" y="1" width="10" height="12"/><path d="M4 5h6M4 8h6"/></svg>
      <div><div style="font-size:5.5px;color:#333;letter-spacing:.5px;margin-bottom:2px">LOREM IPSUM DOLOR</div><p class="lorem">Lorem ipsum dolor sit amet, consectetuer adipiscing elit, sed diam nonummy nibh euismod tincidunt ut laoreet dolore magna aliquam erat volutpat.</p></div></div>
  </div>
  <div class="photo" role="img" aria-label="Laptop mockup showing a red title screen" style="left:300px;top:90px;width:230px;height:140px;background:linear-gradient(180deg,#e30613,#b1000c 80%,#d8d8dc 80%)"></div>
  <div class="abs" style="left:345px;top:172px;width:140px;text-align:center;font-size:6px;color:#fff">Add your text/ picture here and send it to back</div>
</section>

<!-- 13 Wheel & mockups -->
<section class="slide" style="background:#fff">
  <h2 class="title">INFOGRAPHIC WHEEL &amp; MOCKUPS</h2>
  <svg class="abs" style="left:40px;top:56px" width="196" height="196" viewBox="0 0 196 196">
    <g transform="translate(98,98) rotate(-90)">
      <circle r="60" fill="none" stroke="#e30613" stroke-width="68" pathLength="100" stroke-dasharray="12.5 87.5" stroke-dashoffset="0"/>
      <circle r="60" fill="none" stroke="#2b2b2b" stroke-width="68" pathLength="100" stroke-dasharray="12.5 87.5" stroke-dashoffset="-12.5"/>
      <circle r="60" fill="none" stroke="#e30613" stroke-width="68" pathLength="100" stroke-dasharray="12.5 87.5" stroke-dashoffset="-25"/>
      <circle r="60" fill="none" stroke="#2b2b2b" stroke-width="68" pathLength="100" stroke-dasharray="12.5 87.5" stroke-dashoffset="-37.5"/>
      <circle r="60" fill="none" stroke="#e30613" stroke-width="68" pathLength="100" stroke-dasharray="12.5 87.5" stroke-dashoffset="-50"/>
      <circle r="60" fill="none" stroke="#2b2b2b" stroke-width="68" pathLength="100" stroke-dasharray="12.5 87.5" stroke-dashoffset="-62.5"/>
      <circle r="60" fill="none" stroke="#e30613" stroke-width="68" pathLength="100" stroke-dasharray="12.5 87.5" stroke-dashoffset="-75"/>
      <circle r="60" fill="none" stroke="#2b2b2b" stroke-width="68" pathLength="100" stroke-dasharray="12.5 87.5" stroke-dashoffset="-87.5"/>
    </g>
    <circle cx="98" cy="98" r="28" fill="#fff"/>
    <circle cx="98" cy="98" r="20" fill="#e30613"/>
    <g stroke="#fff" stroke-width="1">
      <line x1="98" y1="4" x2="98" y2="70"/><line x1="98" y1="126" x2="98" y2="192"/><line x1="4" y1="98" x2="70" y2="98"/><line x1="126" y1="98" x2="192" y2="98"/>
      <line x1="31" y1="31" x2="78" y2="78"/><line x1="118" y1="118" x2="165" y2="165"/><line x1="165" y1="31" x2="118" y2="78"/><line x1="78" y1="118" x2="31" y2="165"/>
    </g>
  </svg>
  <div class="abs" style="left:254px;top:76px;width:120px">
    <p class="lorem" style="margin-bottom:20px">Lorem Ipsum is simply dummy text of the printing and typesetting industry.</p>
    <p class="lorem" style="margin-bottom:20px">Lorem Ipsum is simply dummy text of the printing and typesetting industry.</p>
    <p class="lorem" style="margin-bottom:20px">Lorem Ipsum is simply dummy text of the printing and typesetting industry.</p>
    <p class="lorem">Lorem Ipsum is simply dummy text of the printing and typesetting industry.</p>
  </div>
  <div class="photo" role="img" aria-label="Smartphone mockup with a red screen" style="left:428px;top:42px;width:110px;height:230px;border-radius:16px;background:linear-gradient(180deg,#f0f0f0 0 10%,#e30613 10% 88%,#f0f0f0 88%)"></div>
  <div class="abs" style="left:446px;top:178px;width:74px;text-align:center;font-size:5.5px;color:#fff">Add your text/ picture here and send it to back</div>
  <footer class="foot"><span class="foot-mark"><i></i>VELORA</span><span>Add your classification details here (Confidential or Public)</span><span class="foot-page">13</span></footer>
</section>

<!-- 14 Tables -->
<section class="slide" style="background:#fff">
  <h2 class="title">TABLES</h2>
  <div class="square" style="left:510px;top:34px;width:30px;height:30px"><svg width="16" height="16" viewBox="0 0 16 16" fill="none" stroke="#fff" stroke-width="1.4"><rect x="2" y="2" width="12" height="12"/><path d="M2 6h12M2 10h12M6 2v12M10 2v12"/></svg></div>
  <table class="data">
    <tr><th class="blank"></th><th>Title here</th><th style="background:none;color:#555">Numbers</th><th>Value</th><th style="background:none;color:#555">Brand</th><th>Quality</th></tr>
    <tr><td class="label">Content type</td><td>Example one</td><td>3</td><td>10</td><td>New</td><td>35%</td></tr>
    <tr><td class="label">Content type</td><td>Example two</td><td>6</td><td>45</td><td>New</td><td>60%</td></tr>
    <tr><td class="label">Content type</td><td class="soft">Example three</td><td>6</td><td class="soft">67</td><td>New</td><td>67%</td></tr>
    <tr><td class="label">Content type</td><td>Example four</td><td>9</td><td>94</td><td>New</td><td>22%</td></tr>
    <tr><td class="label">Content type</td><td>Example five</td><td>2</td><td>50</td><td>New</td><td>55%</td></tr>
    <tr><td class="label">Content type</td><td>Example six</td><td>1</td><td style="outline:1px solid #e30613">90</td><td>New</td><td>09%</td></tr>
    <tr><td class="label">Content type</td><td>Example seven</td><td>5</td><td>31</td><td>New</td><td>30%</td></tr>
  </table>
  <footer class="foot"><span class="foot-mark"><i></i>VELORA</span><span>Add your classification details here (Confidential or Public)</span><span class="foot-page">14</span></footer>
</section>

<!-- 15 Section Management -->
<section class="slide" style="background:#fff">
  <div class="tag">SECTION 02</div>
  <div class="giant" style="font-size:64px;top:60px">MANAGEMENT</div>
  <div class="square" style="left:46px;top:176px;width:34px;height:34px"><svg width="18" height="18" viewBox="0 0 18 18" fill="none" stroke="#fff" stroke-width="1.4"><circle cx="9" cy="5" r="2.5"/><circle cx="4" cy="12" r="2"/><circle cx="14" cy="12" r="2"/><path d="M9 8v2M4 10l5-2 5 2"/></svg></div>
  <p class="abs lorem" style="left:110px;top:178px;width:420px">Lorem ipsum dolor sit amet, consectetuer adipiscing elit, sed diam nonummy nibh euismod tincidunt ut laoreet dolore magna aliquam erat volutpat. Ut wisi enim ad minim veniam, quis nostrud exerci tation ullamcorper suscipit lobortis nisl ut aliquip ex ea commodo consequat. Duis autem vel eum iriure dolor in hendrerit in vulputate velit esse molestie consequat.</p>
  <div class="section-label" style="bottom:36px">MANAGEMENT</div>
</section>

<!-- 16 Management process -->
<section class="slide" style="background:#fff">
  <h2 class="title">MANAGEMENT PROCESS</h2>
  <div class="abs" style="left:8px;right:8px;top:106px;height:1px;background:#999"></div>
  <div class="abs" style="left:0;right:0;top:90px;display:flex;justify-content:space-around;padding:0 18px">
    <div style="width:74px;text-align:center"><div style="width:32px;height:32px;background:var(--red);margin:0 auto 10px"></div><div style="font-family:'Oswald',sans-serif;font-size:8px;color:#333">LOREM IPSUM</div><p class="lorem">Lorem Ipsum is simply dummy text of the printing and typesetting industry.</p></div>
    <div style="width:74px;text-align:center"><div style="width:32px;height:32px;background:var(--red);margin:0 auto 10px"></div><div style="font-family:'Oswald',sans-serif;font-size:8px;color:#333">LOREM IPSUM</div><p class="lorem">Lorem Ipsum is simply dummy text of the printing and typesetting industry.</p></div>
    <div style="width:74px;text-align:center"><div style="width:32px;height:32px;background:var(--red);margin:0 auto 10px"></div><div style="font-family:'Oswald',sans-serif;font-size:8px;color:#333">LOREM IPSUM</div><p class="lorem">Lorem Ipsum is simply dummy text of the printing and typesetting industry.</p></div>
    <div style="width:74px;text-align:center"><div style="width:32px;height:32px;background:var(--red);margin:0 auto 10px;color:#fff;font-family:'Oswald',sans-serif;font-size:18px;line-height:32px">7</div><div style="font-family:'Oswald',sans-serif;font-size:8px;color:#333">LOREM IPSUM</div><p class="lorem">Lorem Ipsum is simply dummy text of the printing and typesetting industry.</p></div>
    <div style="width:74px;text-align:center"><div style="width:32px;height:32px;background:var(--red);margin:0 auto 10px"></div><div style="font-family:'Oswald',sans-serif;font-size:8px;color:#333">LOREM IPSUM</div><p class="lorem">Lorem Ipsum is simply dummy text of the printing and typesetting industry.</p></div>
    <div style="width:74px;text-align:center"><div style="width:32px;height:32px;background:var(--red);margin:0 auto 10px"></div><div style="font-family:'Oswald',sans-serif;font-size:8px;color:#333">LOREM IPSUM</div><p class="lorem">Lorem Ipsum is simply dummy text of the printing and typesetting industry.</p></div>
  </div>
  <footer class="foot"><span class="foot-mark"><i></i>VELORA</span><span>Add your classification details here (Confidential or Public)</span><span class="foot-page">16</span></footer>
</section>

<!-- 17 Our team -->
<section class="slide" style="background:#fff">
  <h2 class="title red">OUR TEAM</h2>
  <div class="abs" style="left:20px;right:20px;top:64px;display:flex;justify-content:space-around">
    <div style="width:100px;text-align:center"><div role="img" aria-label="Portrait photo of a team member" style="width:60px;height:60px;border-radius:50%;background:linear-gradient(#9a9a9a,#4a4a4a);margin:0 auto 14px"></div><div class="small-red" style="font-size:7px">Example Name</div><div style="font-size:5.5px;color:#555;margin-bottom:4px">CEO</div><p class="lorem">There are many variations of passages of lorem ipsum available, but the majority have suffered alteration.</p><div style="font-size:7px;color:#999;margin-top:6px">◯ ◯ ◯</div></div>
    <div style="width:100px;text-align:center"><div role="img" aria-label="Portrait photo of a team member" style="width:60px;height:60px;border-radius:50%;background:linear-gradient(#9a9a9a,#4a4a4a);margin:0 auto 14px"></div><div class="small-red" style="font-size:7px">Example Name</div><div style="font-size:5.5px;color:#555;margin-bottom:4px">Member</div><p class="lorem">There are many variations of passages of lorem ipsum available, but the majority have suffered alteration.</p><div style="font-size:7px;color:#999;margin-top:6px">◯ ◯ ◯</div></div>
    <div style="width:100px;text-align:center"><div role="img" aria-label="Portrait photo of a team member" style="width:60px;height:60px;border-radius:50%;background:linear-gradient(#9a9a9a,#4a4a4a);margin:0 auto 14px"></div><div class="small-red" style="font-size:7px">Example Name</div><div style="font-size:5.5px;color:#555;margin-bottom:4px">Member</div><p class="lorem">There are many variations of passages of lorem ipsum available, but the majority have suffered alteration.</p><div style="font-size:7px;color:#999;margin-top:6px">◯ ◯ ◯</div></div>
    <div style="width:100px;text-align:center"><div role="img" aria-label="Portrait photo of a team member" style="width:60px;height:60px;border-radius:50%;background:linear-gradient(#9a9a9a,#4a4a4a);margin:0 auto 14px"></div><div class="small-red" style="font-size:7px">Example Name</div><div style="font-size:5.5px;color:#555;margin-bottom:4px">Support</div><p class="lorem">There are many variations of passages of lorem ipsum available, but the majority have suffered alteration.</p><div style="font-size:7px;color:#999;margin-top:6px">◯ ◯ ◯</div></div>
  </div>
  <footer class="foot"><span class="foot-mark"><i></i>VELORA</span><span>Add your classification details here (Confidential or Public)</span><span class="foot-page">17</span></footer>
</section>

<!-- 18 Analysis charts -->
<section class="slide" style="background:#fff">
  <h2 class="title">ANALYSIS CHARTS</h2>
  <svg class="abs" style="left:36px;top:60px" width="76" height="76" viewBox="0 0 76 76"><circle cx="38" cy="38" r="32" fill="none" stroke="#e6e6e6" stroke-width="6"/><circle cx="38" cy="38" r="32" fill="none" stroke="#e30613" stroke-width="6" pathLength="100" stroke-dasharray="73 27" transform="rotate(-90 38 38)"/><text x="38" y="44" text-anchor="middle" font-family="Oswald,sans-serif" font-size="17" fill="#333">73%</text></svg>
  <svg class="abs" style="left:36px;top:164px" width="76" height="76" viewBox="0 0 76 76"><circle cx="38" cy="38" r="32" fill="none" stroke="#e6e6e6" stroke-width="6"/><circle cx="38" cy="38" r="32" fill="none" stroke="#e30613" stroke-width="6" pathLength="100" stroke-dasharray="50 50" transform="rotate(-90 38 38)"/><text x="38" y="44" text-anchor="middle" font-family="Oswald,sans-serif" font-size="17" fill="#333">50%</text></svg>
  <div class="abs" style="left:140px;top:84px;width:100px"><div style="font-size:6px;color:#333">Analysis 01</div><p class="lorem">Lorem Ipsum is simply dummy text of the printing and typesetting industry.</p></div>
  <div class="abs" style="left:140px;top:188px;width:100px"><div style="font-size:6px;color:#333">Analysis 02</div><p class="lorem">Lorem Ipsum is simply dummy text of the printing and typesetting industry.</p></div>
  <div class="abs" style="left:280px;top:62px;width:256px;height:200px">
    <div class="bar-row" style="top:0"><span>Analysis 03</span><b>32%</b><div class="track"></div><div class="fill" style="width:32%"></div></div>
    <div class="bar-row" style="top:36px"><span>Analysis 04</span><b>72%</b><div class="track"></div><div class="fill" style="width:72%;background:#bdbdbd"></div></div>
    <div class="bar-row" style="top:72px"><span>Analysis 05</span><b>52%</b><div class="track"></div><div class="fill" style="width:52%"></div></div>
    <div class="bar-row" style="top:108px"><span>Analysis 06</span><b>12%</b><div class="track"></div><div class="fill" style="width:12%"></div></div>
    <div class="bar-row" style="top:144px"><span>Analysis 07</span><b>60%</b><div class="track"></div><div class="fill" style="width:60%"></div></div>
  </div>
  <footer class="foot"><span class="foot-mark"><i></i>VELORA</span><span>Add your classification details here (Confidential or Public)</span><span class="foot-page">18</span></footer>
</section>

<!-- 19 Images with text -->
<section class="slide" style="background:#fff">
  <h2 class="title">IMAGES WITH TEXT</h2>
  <div class="photo" role="img" aria-label="Photo of friends celebrating at a casino party" style="left:24px;top:46px;width:250px;height:108px;background:linear-gradient(120deg,#2a3f6e,#8a3a3a 55%,#c89a6a)"></div>
  <div class="square" style="left:298px;top:50px;width:26px;height:26px"><svg width="14" height="14" viewBox="0 0 14 14"><path d="M4 12h6M5 12V8H3l4-6 4 6H9v4" fill="none" stroke="#fff" stroke-width="1.2"/></svg></div>
  <p class="abs lorem" style="left:298px;top:90px;width:240px">Lorem ipsum dolor sit amet, consectetuer adipiscing elit, sed diam nonummy nibh euismod tincidunt ut laoreet dolore magna aliquam erat volutpat. Ut wisi enim ad minim veniam, quis nostrud exerci tation ullamcorper suscipit lobortis nisl ut aliquip.</p>
  <p class="abs lorem" style="left:32px;top:172px;width:240px">Lorem ipsum dolor sit amet, consectetuer adipiscing elit, sed diam nonummy nibh euismod tincidunt ut laoreet dolore magna aliquam erat volutpat. Ut wisi enim ad minim veniam, quis nostrud exerci tation ullamcorper suscipit lobortis nisl ut aliquip ex ea commodo consequat.</p>
  <div class="photo" role="img" aria-label="Photo of a resort pool terrace with red loungers" style="left:286px;top:160px;width:254px;height:104px;background:linear-gradient(180deg,#a9cfe8,#5d95c2 55%,#b8584f)"></div>
  <footer class="foot"><span class="foot-mark"><i></i>VELORA</span><span>Add your classification details here (Confidential or Public)</span><span class="foot-page">19</span></footer>
</section>

<!-- 20 SWOT -->
<section class="slide" style="background:#fff">
  <h2 class="title">ANALYSIS INFOGRAPHIC</h2>
  <svg class="abs" style="left:222px;top:60px" width="120" height="180" viewBox="0 0 120 180" font-family="Oswald,sans-serif" font-size="11" fill="#333" text-anchor="middle">
    <circle cx="60" cy="90" r="52" fill="none" stroke="#cfcfd2" stroke-width="14"/>
    <circle cx="60" cy="36" r="26" fill="#e30613"/><circle cx="60" cy="144" r="26" fill="#e30613"/><circle cx="18" cy="90" r="22" fill="#e30613"/><circle cx="102" cy="90" r="22" fill="#e30613"/>
    <circle cx="60" cy="36" r="13" fill="#fff"/><circle cx="60" cy="144" r="13" fill="#fff"/><circle cx="18" cy="90" r="11" fill="#fff"/><circle cx="102" cy="90" r="11" fill="#fff"/>
    <text x="60" y="40">S</text><text x="60" y="148">O</text><text x="18" y="94">T</text><text x="102" y="94">W</text>
    <circle cx="60" cy="90" r="14" fill="#e0e0e3"/>
  </svg>
  <div class="abs" style="left:50px;top:70px;width:150px;text-align:right"><div class="small-red" style="font-size:6px">STRENGTH</div><p class="lorem">Lorem ipsum dolor sit amet, consectetuer adipiscing elit, sed diam nonummy nibh euismod tincidunt ut laoreet dolore.</p></div>
  <div class="abs" style="left:364px;top:70px;width:150px"><div class="small-red" style="font-size:6px">WEAKNESS</div><p class="lorem">Lorem ipsum dolor sit amet, consectetuer adipiscing elit, sed diam nonummy nibh euismod tincidunt ut laoreet dolore.</p></div>
  <div class="abs" style="left:50px;top:190px;width:150px;text-align:right"><div class="small-red" style="font-size:6px">THREAT</div><p class="lorem">Lorem ipsum dolor sit amet, consectetuer adipiscing elit, sed diam nonummy nibh euismod tincidunt ut laoreet dolore.</p></div>
  <div class="abs" style="left:364px;top:190px;width:150px"><div class="small-red" style="font-size:6px">OPPORTUNITY</div><p class="lorem">Lorem ipsum dolor sit amet, consectetuer adipiscing elit, sed diam nonummy nibh euismod tincidunt ut laoreet dolore.</p></div>
  <footer class="foot"><span class="foot-mark"><i></i>VELORA</span><span>Add your classification details here (Confidential or Public)</span><span class="foot-page">20</span></footer>
</section>

<!-- 21 Text information -->
<section class="slide" style="background:#fff">
  <h2 class="title">TEXT INFORMATION</h2>
  <div class="num-item" style="left:56px;top:68px"><div class="n">1</div><h4>TEXT INFORMATION</h4><p class="lorem">Lorem ipsum dolor sit amet, consectetuer adipiscing elit, sed diam nonummy nibh euismod tincidunt ut laoreet dolore magna.</p></div>
  <div class="num-item" style="left:56px;top:132px"><div class="n">2</div><h4>TEXT INFORMATION</h4><p class="lorem">Lorem ipsum dolor sit amet, consectetuer adipiscing elit, sed diam nonummy nibh euismod tincidunt ut laoreet dolore magna.</p></div>
  <div class="num-item" style="left:56px;top:196px"><div class="n">3</div><h4>TEXT INFORMATION</h4><p class="lorem">Lorem ipsum dolor sit amet, consectetuer adipiscing elit, sed diam nonummy nibh euismod tincidunt ut laoreet dolore magna.</p></div>
  <div class="num-item" style="left:306px;top:68px"><div class="n">4</div><h4>TEXT INFORMATION</h4><p class="lorem">Lorem ipsum dolor sit amet, consectetuer adipiscing elit, sed diam nonummy nibh euismod tincidunt ut laoreet dolore magna.</p></div>
  <div class="num-item" style="left:306px;top:132px"><div class="n">5</div><h4>TEXT INFORMATION</h4><p class="lorem">Lorem ipsum dolor sit amet, consectetuer adipiscing elit, sed diam nonummy nibh euismod tincidunt ut laoreet dolore magna.</p></div>
  <div class="num-item" style="left:306px;top:196px"><div class="n">6</div><h4>TEXT INFORMATION</h4><p class="lorem">Lorem ipsum dolor sit amet, consectetuer adipiscing elit, sed diam nonummy nibh euismod tincidunt ut laoreet dolore magna.</p></div>
  <footer class="foot"><span class="foot-mark"><i></i>VELORA</span><span>Add your classification details here (Confidential or Public)</span><span class="foot-page">21</span></footer>
</section>

<!-- 22 Infographic ABC -->
<section class="slide" style="background:#fff">
  <h2 class="title">INFOGRAPHIC</h2>
  <svg class="abs" style="left:186px;top:54px" width="190" height="210" viewBox="0 0 190 210" font-family="Oswald,sans-serif" font-size="11" fill="#333" text-anchor="middle">
    <circle cx="95" cy="62" r="42" fill="#e30613"/><circle cx="50" cy="142" r="42" fill="#e30613"/><circle cx="140" cy="142" r="42" fill="#e30613"/>
    <circle cx="95" cy="62" r="18" fill="#fff"/><circle cx="50" cy="142" r="18" fill="#fff"/><circle cx="140" cy="142" r="18" fill="#fff"/>
    <circle cx="95" cy="115" r="10" fill="#2b2b2b"/><circle cx="95" cy="115" r="4" fill="#fff"/>
    <text x="95" y="66">A</text><text x="50" y="146">C</text><text x="140" y="146">B</text>
    <circle cx="38" cy="72" r="6" fill="#2b2b2b"/><circle cx="152" cy="40" r="6" fill="#2b2b2b"/><circle cx="176" cy="110" r="6" fill="#2b2b2b"/>
  </svg>
  <div class="abs" style="left:60px;top:118px;width:150px;text-align:right"><div class="small-red" style="font-size:6px">TEXT INFORMATION</div><p class="lorem">Lorem ipsum dolor sit amet, consectetuer adipiscing elit, sed diam nonummy nibh euismod tincidunt ut laoreet.</p></div>
  <div class="abs" style="left:360px;top:86px;width:150px"><div class="small-red" style="font-size:6px">TEXT INFORMATION</div><p class="lorem">Lorem ipsum dolor sit amet, consectetuer adipiscing elit, sed diam nonummy nibh euismod tincidunt ut laoreet.</p></div>
  <div class="abs" style="left:384px;top:156px;width:150px"><div class="small-red" style="font-size:6px">TEXT INFORMATION</div><p class="lorem">Lorem ipsum dolor sit amet, consectetuer adipiscing elit, sed diam nonummy nibh euismod tincidunt ut laoreet.</p></div>
  <footer class="foot"><span class="foot-mark"><i></i>VELORA</span><span>Add your classification details here (Confidential or Public)</span><span class="foot-page">22</span></footer>
</section>

<!-- 23 Infographic hub -->
<section class="slide" style="background:#fff">
  <h2 class="title">INFOGRAPHIC</h2>
  <svg class="abs" style="left:0;top:40px" width="564" height="230" viewBox="0 0 564 230" fill="none">
    <g stroke="#333" stroke-dasharray="2 2" stroke-width=".8">
      <path d="M140 45h90l30 40"/><path d="M140 118h90"/><path d="M140 190h90l30-40"/>
      <path d="M424 45h-90l-30 40"/><path d="M424 118h-90"/><path d="M424 190h-90l-30-40"/>
    </g>
    <circle cx="282" cy="118" r="62" fill="#fff" stroke="#e30613" stroke-width="2"/>
    <circle cx="282" cy="118" r="48" fill="#f3f3f5"/>
    <text x="282" y="123" text-anchor="middle" font-family="Oswald,sans-serif" font-size="14" fill="#e30613">VELORA</text>
  </svg>
  <div class="square" style="left:110px;top:70px;width:30px;height:30px"></div>
  <div class="square" style="left:110px;top:143px;width:30px;height:30px"></div>
  <div class="square" style="left:110px;top:215px;width:30px;height:30px"></div>
  <div class="square" style="left:424px;top:70px;width:30px;height:30px"></div>
  <div class="square" style="left:424px;top:143px;width:30px;height:30px"></div>
  <div class="square" style="left:424px;top:215px;width:30px;height:30px"></div>
  <div class="abs" style="left:160px;top:64px;width:70px"><div class="small-red" style="font-size:6px">LOREM IPSUM</div><p class="lorem">Lorem ipsum dolor sit amet consectetuer.</p></div>
  <div class="abs" style="left:160px;top:138px;width:70px"><div class="small-red" style="font-size:6px">LOREM IPSUM</div><p class="lorem">Lorem ipsum dolor sit amet consectetuer.</p></div>
  <div class="abs" style="left:160px;top:210px;width:70px"><div class="small-red" style="font-size:6px">LOREM IPSUM</div><p class="lorem">Lorem ipsum dolor sit amet consectetuer.</p></div>
  <div class="abs" style="left:340px;top:64px;width:70px;text-align:right"><div class="small-red" style="font-size:6px">LOREM IPSUM</div><p class="lorem">Lorem ipsum dolor sit amet consectetuer.</p></div>
  <div class="abs" style="left:340px;top:138px;width:70px;text-align:right"><div class="small-red" style="font-size:6px">LOREM IPSUM</div><p class="lorem">Lorem ipsum dolor sit amet consectetuer.</p></div>
  <div class="abs" style="left:340px;top:210px;width:70px;text-align:right"><div class="small-red" style="font-size:6px">LOREM IPSUM</div><p class="lorem">Lorem ipsum dolor sit amet consectetuer.</p></div>
  <footer class="foot"><span class="foot-mark"><i></i>VELORA</span><span>Add your classification details here (Confidential or Public)</span><span class="foot-page">23</span></footer>
</section>

<!-- 24 Locations Austria -->
<section class="slide" style="background:#fff">
  <h2 class="title">LOCATIONS - IN AUSTRIA</h2>
  <div class="photo" role="img" aria-label="Outline map of Austria with a highlighted red region and location pins" style="left:22px;top:74px;width:286px;height:164px;background:linear-gradient(90deg,#ececef,#f4d3d5 45%,#ececef)"></div>
  <div class="abs" style="left:320px;top:80px;width:1px;height:170px;background:var(--red)"></div>
  <div class="square" style="left:334px;top:80px;width:28px;height:28px"><svg width="14" height="14" viewBox="0 0 14 14"><path d="M7 13S2 8 2 5a5 5 0 0 1 10 0c0 3-5 8-5 8Z" fill="#fff"/><circle cx="7" cy="5" r="2" fill="#e30613"/></svg></div>
  <div class="abs" style="left:370px;top:82px;width:170px"><div class="small-red" style="font-size:6px">AUSTRIA EDITABLE MAP</div><p class="lorem">Lorem ipsum dolor sit amet, consectetuer adipiscing elit.</p></div>
  <svg class="abs" style="left:336px;top:134px" width="64" height="64" viewBox="0 0 64 64"><circle cx="32" cy="32" r="27" fill="none" stroke="#e6e6e6" stroke-width="5"/><circle cx="32" cy="32" r="27" fill="none" stroke="#e30613" stroke-width="5" pathLength="100" stroke-dasharray="50 50" transform="rotate(-90 32 32)"/><text x="32" y="37" text-anchor="middle" font-family="Oswald,sans-serif" font-size="14" fill="#333">50%</text></svg>
  <div class="abs" style="left:410px;top:146px;width:130px"><div style="font-size:6px;color:#333">INFOGRAPHICS</div><p class="lorem">Lorem Ipsum is simply dummy text of the printing and typesetting industry.</p></div>
  <svg class="abs" style="left:410px;top:200px" width="40" height="26" viewBox="0 0 40 26" fill="#555"><circle cx="10" cy="4" r="3"/><path d="M6 9h8l-1 9h-2v7H9v-7H7Z"/><circle cx="30" cy="4" r="3"/><path d="M26 9h8l2 10h-3v6h-6v-6h-3Z"/></svg>
  <footer class="foot"><span class="foot-mark"><i></i>VELORA</span><span>Add your classification details here (Confidential or Public)</span><span class="foot-page">24</span></footer>
</section>

<!-- 25 Locations International -->
<section class="slide" style="background:#fff">
  <h2 class="title">LOCATIONS - INTERNATIONAL</h2>
  <div class="square" style="left:118px;top:62px;width:28px;height:28px"><svg width="14" height="14" viewBox="0 0 14 14"><path d="M7 13S2 8 2 5a5 5 0 0 1 10 0c0 3-5 8-5 8Z" fill="#fff"/><circle cx="7" cy="5" r="2" fill="#e30613"/></svg></div>
  <div class="abs" style="left:26px;top:94px;width:120px"><div class="small-red" style="font-size:6px">WORLD EDITABLE MAP</div><p class="lorem">Lorem ipsum dolor sit amet, consectetuer adipiscing elit.</p></div>
  <div class="abs" style="left:26px;top:130px;width:120px;height:50px">
    <div class="bar-row" style="top:0"><span>MEN</span><b>70%</b><div class="track"></div><div class="fill" style="width:70%"></div></div>
    <div class="bar-row" style="top:20px"><span>WOMEN</span><b>30%</b><div class="track"></div><div class="fill" style="width:30%"></div></div>
  </div>
  <svg class="abs" style="left:28px;top:190px" width="40" height="26" viewBox="0 0 40 26" fill="#555"><circle cx="10" cy="4" r="3"/><path d="M6 9h8l-1 9h-2v7H9v-7H7Z"/><circle cx="30" cy="4" r="3"/><path d="M26 9h8l2 10h-3v6h-6v-6h-3Z"/></svg>
  <div class="photo" role="img" aria-label="Dotted world map with red location pins" style="left:196px;top:56px;width:344px;height:196px;background:linear-gradient(135deg,#ececef,#f2dfe0 50%,#ececef)"></div>
  <footer class="foot"><span class="foot-mark"><i></i>VELORA</span><span>Add your classification details here (Confidential or Public)</span><span class="foot-page">25</span></footer>
</section>

<!-- 26 Icons -->
<section class="slide" style="background:#fff">
  <div class="abs" style="left:30px;top:28px;font-family:'Oswald',sans-serif;font-size:13px;color:#333">FREE VECTOR ICON LINKS AVAILABLE</div>
  <div class="photo" role="img" aria-label="Grid of red and grey line icons" style="left:30px;top:60px;width:504px;height:240px;background:linear-gradient(135deg,#f4d3d5,#ececef 50%,#f4d3d5)"></div>
</section>

<!-- 27 Get in touch -->
<section class="slide" style="background:var(--red)">
  <div class="abs" style="left:280px;top:0;width:330px;height:319px;border-radius:50%;background:rgba(255,255,255,.08)"></div>
  <div class="brand-disc" style="left:312px;top:66px;width:200px;height:200px;background:#fff;color:var(--red);font-size:24px">VELORA</div>
  <div class="abs" style="left:34px;top:160px;font-family:'Oswald',sans-serif;font-size:12px;color:#fff;letter-spacing:.5px">GET IN TOUCH</div>
  <ul class="abs" style="left:34px;top:190px;list-style:none;font-size:6px;color:#fff;line-height:26px">
    <li><svg width="10" height="10" viewBox="0 0 10 10" style="vertical-align:middle;margin-right:14px"><circle cx="5" cy="5" r="4" fill="none" stroke="#fff"/><path d="M1 5h8M5 1v8" stroke="#fff" stroke-width=".6"/></svg>www.veloragaming.example</li>
    <li><svg width="10" height="10" viewBox="0 0 10 10" style="vertical-align:middle;margin-right:14px"><path d="M2 1h2l1 2-1 1a5 5 0 0 0 2 2l1-1 2 1v2c-4 1-8-3-7-7Z" fill="#fff"/></svg>+00 123 456 789</li>
    <li><svg width="10" height="10" viewBox="0 0 10 10" style="vertical-align:middle;margin-right:14px"><rect x="1" y="2" width="8" height="6" fill="none" stroke="#fff"/><path d="M1 2l4 3 4-3" fill="none" stroke="#fff"/></svg>hello@veloragaming.example</li>
    <li><svg width="10" height="10" viewBox="0 0 10 10" style="vertical-align:middle;margin-right:14px"><path d="M5 9S2 6 2 4a3 3 0 0 1 6 0c0 2-3 5-3 5Z" fill="#fff"/></svg>Add Your Address, Street, road, here</li>
  </ul>
</section>

<!-- 28 Closing -->
<section class="slide" style="background:var(--stone)">
  <div class="brand-disc" style="left:196px;top:60px;width:172px;height:172px;font-size:22px">VELORA</div>
  <div class="abs" style="left:0;right:0;top:262px;text-align:center;font-size:7px;letter-spacing:1px;color:#555">WWW.VELORAGAMING.EXAMPLE</div>
</section>

</main>
</body>
</html>
```